Business Card Design

Contact Information for Business Card

A vertical business card request- a medium & light gray with silverfern tree logo (logo is attached)

Please use Trebuchet font -- if possible- can we use two different color gray? (See pictures attached below)
Info on the front should be the Silverfern tree logo - on the top of the card, followed by the info ...
Card to read: " " indicated what should be on the card --
Name: " Joan Pelley "
Title : "Partner "
" Office: 202.555.0147 "
" Mobile: 202.555.0182 "

Backside of the card - solid medium color gray color w/ address and small message centered in the card - Trebuchet font
to read:

" 317 B North Linden Avenue, NE "
" Washington, DC 20099 "

Then below address to read:
" Fundraising | Event Planning | Political Consulting "

```html
<!DOCTYPE html>
<html lang="en">
<head>
<meta charset="utf-8">
<title>Silverfern Strategies – Business Card</title>
<link href="https://fonts.googleapis.com/css2?family=Fira+Sans:wght@300;400;600&display=swap" rel="stylesheet">
<style>
  :root {
    --backdrop: #2b2b2b;
    --gray-top: #8c8c8c;
    --gray-mid: #6f6f6f;
    --gray-bottom: #666666;
    --card-light: #e9e9e9;
    --ink-dark: #262626;
    --ink-soft: #333333;
    --brand-light: #e4e4e4;
    --mark-fill: #bdbdbd;
    --rule-light: #ececec;
  }
  * { margin: 0; padding: 0; box-sizing: border-box; }
  html, body {
    width: 1200px;
    height: 900px;
    overflow: hidden;
    background: var(--backdrop);
    font-family: "Fira Sans", "Trebuchet MS", sans-serif;
  }
  .stage { position: relative; width: 1200px; height: 900px; }
  .card {
    position: absolute;
    top: 219px;
    width: 279px;
    height: 488px;
    overflow: hidden;
  }
  .card--front { left: 286px; background: var(--card-light); }
  .card--back {
    left: 632px;
    background: linear-gradient(180deg, var(--gray-top) 0%, var(--gray-mid) 45%, var(--gray-bottom) 100%);
  }
  .brand-panel {
    position: absolute;
    left: 0; top: 0;
    width: 100%;
    height: 279px;
    background: linear-gradient(180deg, var(--gray-top) 0%, var(--gray-mid) 100%);
  }
  .card--back .brand-panel { background: transparent; }
  .brand-mark {
    position: absolute;
    left: 102px;
    top: 56px;
    width: 136px;
    height: 136px;
    background: var(--mark-fill);
    opacity: 0.55;
  }
  .brand-name {
    position: absolute;
    right: 14px;
    top: 202px;
    text-align: right;
    color: var(--brand-light);
    font-weight: 300;
    text-transform: uppercase;
    line-height: 1;
  }
  .brand-name__main { display: block; font-size: 30px; letter-spacing: 0.5px; }
  .brand-name__sub { display: block; font-size: 16px; letter-spacing: 1px; margin-top: 6px; }
  .divider {
    position: absolute;
    left: 0; top: 279px;
    width: 100%; height: 4px;
    background: var(--rule-light);
  }
  .contact {
    position: absolute;
    left: 16px;
    top: 327px;
    color: var(--ink-soft);
  }
  .contact__name { font-size: 19px; font-weight: 600; color: var(--ink-dark); line-height: 1.2; }
  .contact__title { font-size: 14px; line-height: 1.3; }
  .contact__lines { margin-top: 34px; font-size: 15px; line-height: 18.5px; }
  .address {
    position: absolute;
    left: 0; top: 356px;
    width: 100%;
    text-align: center;
    color: var(--brand-light);
  }
  .address__lines { font-size: 15px; line-height: 18.5px; }
  .address__services {
    margin-top: 20px;
    font-size: 8.5px;
    letter-spacing: 0.3px;
    text-transform: uppercase;
  }
</style>
</head>
<body>
<main class="stage">
  <section class="card card--front" aria-label="Card front">
    <div class="brand-panel">
      <div class="brand-mark" role="img" aria-label="Silverfern brand mark area"></div>
      <p class="brand-name">
        <span class="brand-name__main">Silverfern</span>
        <span class="brand-name__sub">Strategies</span>
      </p>
    </div>
    <div class="contact">
      <p class="contact__name">Joan Pelley</p>
      <p class="contact__title">Partner</p>
      <p class="contact__lines">
        202.555.0147 office<br>
        202.555.0182 mobile<br>
        joan@silverfernllc.com
      </p>
    </div>
  </section>

  <section class="card card--back" aria-label="Card back">
    <div class="brand-panel">
      <div class="brand-mark" role="img" aria-label="Silverfern brand mark area"></div>
      <p class="brand-name">
        <span class="brand-name__main">Silverfern</span>
        <span class="brand-name__sub">Strategies</span>
      </p>
    </div>
    <div class="divider"></div>
    <div class="address">
      <p class="address__lines">
        317 B North Linden Avenue, NE<br>
        Washington, DC 20099
      </p>
      <p class="address__services">Fundraising | Event Planning | Political Consulting</p>
    </div>
  </section>
</main>
</body>
</html>
```